Business Card Design Needed

Business car design required, logo will be supplied.

Brambleford Power Surveyors are looking to become the leading provider of energy performance certificates to estate agents, landlords and home owners in the Yorkshire region of the UK.

The business card must be double sided and professional looking. Estate agents receive hundreds of cards from contractors and our card must stand out.

I require a two sided business card that is clean, modern and created by a designer that can think outside of the box.

Brand colours can be supplied .

Please ask if you have any questions.

Target Market(s)

Estate agents, landlords and property owners

Industry/Entity Type

Property - estate agency - energy consultants

Contact Information for Business Card

Tomas Rendell - Energy Assessor - 07311642705 - www.BramblefordPSV.co.uk - info@bramblefordpsv.co.uk

Font styles to use
Serif
Sans Serif

Colors
00AB8E
00BBA5
67D7C9
C6EFE9
E9F9F6

Requirements
Must have
• Use the provided logo, clean, professional and stand out from the crowd
Nice to have
• Clever use of text, spacing and brand colours
Should not have
• Clip art

```html
<!DOCTYPE html>
<html lang="en">
<head>
<meta charset="utf-8">
<title>Brambleford Power Surveyors – Business Card</title>
<link href="https://fonts.googleapis.com/css2?family=Marcellus&display=swap" rel="stylesheet">
<style>
  :root {
    --brand-blue: #14629f;
    --brand-blue-deep: #0f5891;
    --brand-lime: #a9c62b;
    --paper: #ffffff;
    --paper-shade: #eef1f4;
    --faint-ring: #dde6ee;
    --stage: #e4e6e9;
    --text-light: #ffffff;
  }
  * { box-sizing: border-box; margin: 0; padding: 0; }
  html, body {
    width: 1200px; height: 900px; overflow: hidden;
    background: var(--stage);
    font-family: "Marcellus", "Optima", serif;
  }
  .canvas { position: relative; width: 1200px; height: 900px; }

  .card {
    position: absolute;
    width: 620px; height: 354px;
    border-radius: 34px;
    overflow: hidden;
    box-shadow: 0 10px 26px rgba(0,0,0,.18);
  }

  /* Front */
  .card-front { left: 120px; top: 70px; background: var(--brand-blue); }
  .front-brand {
    position: absolute; left: 0; right: 0; top: 50%;
    transform: translateY(-50%);
    display: flex; align-items: center; justify-content: center; gap: 22px;
    color: var(--text-light);
  }
  .brand-dot {
    width: 64px; height: 64px; border-radius: 50%;
    border: 5px solid var(--text-light);
  }
  .brand-divider { width: 1px; height: 74px; background: rgba(255,255,255,.7); }
  .brand-name { line-height: 1; text-transform: uppercase; }
  .brand-name .line-main { display: block; font-size: 40px; letter-spacing: 1px; }
  .brand-name .line-sub { display: block; font-size: 15px; letter-spacing: 6px; margin-top: 8px; }

  /* Back */
  .card-back {
    left: 460px; top: 476px;
    background: linear-gradient(120deg, var(--paper-shade), var(--paper) 60%);
  }
  .back-shapes { position: absolute; inset: 0; }

  .back-brand {
    position: absolute; right: 30px; top: 30px;
    display: flex; align-items: center; gap: 12px;
    color: var(--brand-blue);
  }
  .back-brand .brand-dot { width: 40px; height: 40px; border-width: 4px; border-color: var(--brand-blue); }
  .back-brand .brand-divider { height: 46px; background: var(--brand-blue); }
  .back-brand .line-main { font-size: 25px; }
  .back-brand .line-sub { font-size: 10px; letter-spacing: 3.5px; margin-top: 5px; }

  .person { position: absolute; left: 62px; top: 120px; }
  .person-name {
    color: var(--brand-lime); font-size: 27px;
    text-transform: uppercase; letter-spacing: .5px;
  }
  .person-role { color: var(--text-light); font-size: 19px; margin-top: 2px; }

  .contact-list {
    position: absolute; left: 62px; top: 236px;
    list-style: none; color: var(--text-light); font-size: 16px;
  }
  .contact-list li { display: flex; align-items: center; gap: 10px; height: 27px; }
  .contact-icon { width: 16px; height: 16px; fill: var(--brand-lime); flex: none; }
</style>
</head>
<body>
<main class="canvas">

  <section class="card card-front" aria-label="Business card front">
    <div class="front-brand">
      <span class="brand-dot"></span>
      <span class="brand-divider"></span>
      <span class="brand-name">
        <span class="line-main">Brambleford</span>
        <span class="line-sub">Power Surveyors</span>
      </span>
    </div>
  </section>

  <section class="card card-back" aria-label="Business card back">
    <svg class="back-shapes" width="620" height="354" viewBox="0 0 620 354">
      <circle cx="520" cy="220" r="150" fill="none" stroke="var(--faint-ring)" stroke-width="22" opacity=".8"/>
      <path d="M0 0 H215 C330 60 390 200 370 354 H0 Z" fill="var(--brand-blue)"/>
      <path d="M130 20 C250 60 320 180 320 354" fill="none" stroke="var(--brand-blue-deep)" stroke-width="3"/>
    </svg>

    <div class="back-brand">
      <span class="brand-dot"></span>
      <span class="brand-divider"></span>
      <span class="brand-name">
        <span class="line-main">Brambleford</span>
        <span class="line-sub">Power Surveyors</span>
      </span>
    </div>

    <div class="person">
      <p class="person-name">Tomas Rendell</p>
      <p class="person-role">Energy Assessor</p>
    </div>

    <ul class="contact-list">
      <li>
        <svg class="contact-icon" viewBox="0 0 16 16" aria-hidden="true"><path d="M3 1.5l3 3-1.6 1.8c.8 1.9 2.3 3.4 4.3 4.3L10.5 9l3 3-2 2.5C6.3 14 2 9.7 1.5 4.5z"/></svg>
        <span>07311642705</span>
      </li>
      <li>
        <svg class="contact-icon" viewBox="0 0 16 16" aria-hidden="true"><path d="M1 3h14v10H1z M2.2 4.2L8 8.6l5.8-4.4" stroke="var(--brand-blue)" stroke-width="1"/></svg>
        <span>info@bramblefordpsv.co.uk</span>
      </li>
      <li>
        <svg class="contact-icon" viewBox="0 0 16 16" aria-hidden="true"><circle cx="8" cy="8" r="7"/><path d="M1 8h14M8 1c-3 3.5-3 10.5 0 14M8 1c3 3.5 3 10.5 0 14" fill="none" stroke="var(--brand-blue)" stroke-width="1"/></svg>
        <span>www.BramblefordPSV.co.uk</span>
      </li>
    </ul>
  </section>

</main>
</body>
</html>
```